Moravel Stenwick Inc needs a business card design

Looking for a unique, classy and sharp business card design.

Contact Information for Business Card

Moravel Stenwick Inc.
Marisa Ortega Bellido BScOT(c)
Occupational Therapist
(780) 555-0142
moravelstenwick@postlynx.net

```html
<!DOCTYPE html>
<html lang="en">
<head>
<meta charset="utf-8">
<title>Moravel Stenwick Inc. – Business Card</title>
<link rel="stylesheet" href="https://fonts.googleapis.com/css2?family=Open+Sans:wght@400;700&family=Pinyon+Script&family=Libre+Baskerville&display=swap">
<style>
  :root {
    --leaf-light: #dff0c8;
    --leaf-mid: #b9de8e;
    --leaf-deep: #4c9c3e;
    --glow: #fffbe0;
    --ink: #1d1d1d;
    --ink-soft: #333333;
    --brand: #8b2f8c;
    --white: #ffffff;
    --petal: #d9b6e0;
  }
  html, body {
    margin: 0;
    padding: 0;
    width: 720px;
    height: 1200px;
    overflow: hidden;
    background: #ffffff;
  }
  .card {
    position: relative;
    width: 720px;
    height: 1200px;
    overflow: hidden;
  }
  .card__art {
    position: absolute;
    inset: 0;
    width: 720px;
    height: 1200px;
  }
  .brand-name {
    position: absolute;
    left: 0;
    width: 720px;
    top: 244px;
    text-align: center;
    font-family: "Open Sans", sans-serif;
    font-weight: 700;
    font-size: 38px;
    letter-spacing: -0.5px;
    color: var(--brand);
    margin: 0;
  }
  .person {
    position: absolute;
    left: 180px;
    width: 420px;
    top: 432px;
    text-align: center;
    font-family: "Pinyon Script", cursive;
    font-weight: 400;
    font-size: 42px;
    line-height: 50px;
    color: var(--ink);
    margin: 0;
  }
  .role {
    position: absolute;
    left: 150px;
    width: 470px;
    top: 540px;
    text-align: center;
    font-family: "Libre Baskerville", serif;
    font-size: 27px;
    color: var(--ink);
    margin: 0;
  }
  .rule {
    position: absolute;
    left: 123px;
    width: 518px;
    height: 0;
    border-top: 1.5px solid var(--ink);
  }
  .rule--top { top: 582px; }
  .rule--bottom { top: 822px; }
  .contact {
    position: absolute;
    left: 127px;
    display: flex;
    align-items: center;
    gap: 48px;
    font-family: "Open Sans", sans-serif;
    font-size: 22px;
    color: var(--ink-soft);
  }
  .contact--phone { top: 618px; }
  .contact--email { top: 712px; }
  .contact__icon { width: 52px; height: 52px; flex: none; }
</style>
</head>
<body>
<main class="card">
  <svg class="card__art" viewBox="0 0 720 1200" xmlns="http://www.w3.org/2000/svg">
    <defs>
      <linearGradient id="bg-wash" x1="0" y1="0" x2="1" y2="1">
        <stop offset="0" stop-color="#b5da7c"/>
        <stop offset="0.45" stop-color="#d9eec2"/>
        <stop offset="1" stop-color="#cfe6b6"/>
      </linearGradient>
      <radialGradient id="sun-glow" cx="0.8" cy="0.03" r="0.45">
        <stop offset="0" stop-color="#fffdf0"/>
        <stop offset="1" stop-color="#fffdf0" stop-opacity="0"/>
      </radialGradient>
      <radialGradient id="logo-halo" cx="0.5" cy="0.5" r="0.5">
        <stop offset="0" stop-color="#ffffff" stop-opacity="0.85"/>
        <stop offset="1" stop-color="#ffffff" stop-opacity="0"/>
      </radialGradient>
    </defs>

    <g role="img" aria-label="Photograph of sunlit green leaves with soft bokeh light">
      <rect width="720" height="1200" fill="url(#bg-wash)"/>
      <rect width="720" height="1200" fill="url(#sun-glow)"/>
      <ellipse cx="110" cy="330" rx="150" ry="300" fill="var(--leaf-mid)" opacity="0.55"/>
      <ellipse cx="380" cy="1180" rx="420" ry="60" fill="#9fc98a" opacity="0.5"/>
    </g>

    <ellipse cx="360" cy="250" rx="230" ry="120" fill="url(#logo-halo)"/>

    <path class="curve curve--main" d="M215 0 C165 130 205 260 340 330 C540 440 665 720 712 1200" fill="none" stroke="var(--leaf-deep)" stroke-width="14"/>
    <path class="curve curve--thin" d="M0 292 C140 272 260 276 370 310" fill="none" stroke="var(--leaf-deep)" stroke-width="9"/>
    <path class="swoosh" d="M45 320 C260 280 520 350 720 560 L720 640 C560 430 300 325 45 320 Z" fill="var(--white)"/>
    <path class="curve curve--lower" d="M0 905 C200 820 490 830 720 1085" fill="none" stroke="var(--leaf-deep)" stroke-width="14"/>

    <g role="img" aria-label="White butterfly ornament">
      <ellipse cx="170" cy="490" rx="60" ry="70" fill="var(--white)" opacity="0.8"/>
    </g>
    <g role="img" aria-label="Green butterfly ornament">
      <ellipse cx="150" cy="1030" rx="70" ry="80" fill="var(--leaf-deep)" opacity="0.85"/>
    </g>
    <g role="img" aria-label="Photograph of a pale pink daisy">
      <ellipse cx="700" cy="960" rx="70" ry="22" fill="var(--petal)" opacity="0.8"/>
    </g>
  </svg>

  <p class="brand-name">Moravel Stenwick Inc.</p>

  <h1 class="person">Marisa Ortega<br>Bellido</h1>
  <p class="role">Occupational Therapist</p>

  <div class="rule rule--top"></div>

  <div class="contact contact--phone">
    <svg class="contact__icon" viewBox="0 0 24 24" aria-hidden="true">
      <path d="M6.6 10.8a15.1 15.1 0 0 0 6.6 6.6l2.2-2.2a1 1 0 0 1 1-.25 11.4 11.4 0 0 0 3.6.57 1 1 0 0 1 1 1V20a1 1 0 0 1-1 1A17 17 0 0 1 3 4a1 1 0 0 1 1-1h3.5a1 1 0 0 1 1 1c0 1.25.2 2.45.57 3.57a1 1 0 0 1-.25 1z" fill="var(--ink)" transform="rotate(-10 12 12)"/>
    </svg>
    <span>(780) 555-0142</span>
  </div>

  <div class="contact contact--email">
    <svg class="contact__icon" viewBox="0 0 24 24" aria-hidden="true">
      <circle cx="12" cy="12" r="10" fill="var(--ink)"/>
      <g fill="none" stroke="#cfe6b6" stroke-width="1.1">
        <ellipse cx="12" cy="12" rx="4.2" ry="9.5"/>
        <line x1="12" y1="2.5" x2="12" y2="21.5"/>
        <line x1="2.5" y1="12" x2="21.5" y2="12"/>
        <path d="M4 7h16M4 17h16"/>
      </g>
    </svg>
    <span>moravelstenwick@postlynx.net</span>
  </div>

  <div class="rule rule--bottom"></div>
</main>
</body>
</html>
```